Acupuncture Medspa needs a business card design

I need a business card design that looks professional, has a spa-like quality and can offer a promo on the back. Initial promo is "First session free". The tagline of NeedleNook is: Refresh, Restore, Rejuvenate.

NeedleNook is a membership-based acupuncture medspa that offers acupuncture, cupping, and herbal therapies. Members choose between the "Refresh" membership which is for stress relief, or "Restore" which is for treating health conditions, and lastly "Rejuvenate" which is for natural facial enhancement.

Industry/Entity Type

Health And Wellness

Contact Information for Business Card

Coral Haskins, MAC, L.Ac.
612-555-0193
www.needlenook-example.com

Font styles to use
Serif
Sans Serif

Colors

Designer to choose colors to be used in the design.

Requirements
Must have
• The project must have NeedleNook logo, promo on the back, and contact information
Nice to have
• I would like to see the colors of the logo used.

```html
<!DOCTYPE html>
<html lang="en">
<head>
<meta charset="utf-8">
<title>NeedleNook Business Card</title>
<link rel="stylesheet" href="https://fonts.googleapis.com/css2?family=Open+Sans:wght@400;600;700&family=Lato:wght@400&display=swap">
<style>
  :root {
    --stage: #6a6a6a;
    --card-white: #ffffff;
    --teal: #158a84;
    --teal-line: #2a9a93;
    --ink: #2b1b14;
    --text: #333333;
  }
  * { margin: 0; padding: 0; box-sizing: border-box; }
  html, body { width: 1200px; height: 1200px; overflow: hidden; }
  body { background: var(--stage); position: relative; font-family: "Open Sans", sans-serif; }

  .card {
    position: absolute;
    left: 240px;
    width: 720px;
    height: 420px;
    border-radius: 34px;
    overflow: hidden;
  }
  .card-front { top: 142px; background: var(--card-white); }
  .card-back { top: 638px; background: var(--teal); }

  .brand {
    position: absolute;
    display: flex;
    align-items: center;
    gap: 12px;
    font-family: "Open Sans", sans-serif;
    font-weight: 600;
    white-space: nowrap;
  }
  .brand-dot { border-radius: 50%; flex: none; }
  .card-front .brand { left: 26px; top: 50px; color: var(--teal); font-size: 42px; }
  .card-front .brand-dot { width: 18px; height: 18px; background: var(--teal); }
  .card-back .brand { left: 0; right: 0; justify-content: center; top: 190px; color: #ffffff; font-size: 62px; }
  .card-back .brand-dot { width: 24px; height: 24px; background: #ffffff; }

  .holder-name {
    position: absolute; right: 22px; top: 164px;
    font-weight: 700; font-size: 24px; color: var(--ink);
  }
  .divider {
    position: absolute; left: 26px; top: 213px;
    width: 554px; height: 2px; background: var(--teal-line);
  }
  .credentials {
    position: absolute; right: 22px; top: 199px;
    font-weight: 600; font-size: 18px; color: var(--teal);
  }
  .contact-list { position: absolute; left: 30px; top: 289px; list-style: none; }
  .contact-list li {
    display: flex; align-items: center; gap: 10px;
    height: 27px; font-size: 17px; color: var(--text);
  }
  .contact-list svg { width: 13px; height: 13px; flex: none; }

  .promo {
    position: absolute; left: 0; right: 0; top: 364px;
    text-align: center; font-family: "Lato", sans-serif;
    font-size: 22px; color: #ffffff; letter-spacing: 0.3px;
  }
</style>
</head>
<body>
  <section class="card card-front">
    <div class="brand"><span class="brand-dot"></span>NeedleNook</div>
    <div class="holder-name">Coral Haskins</div>
    <div class="divider"></div>
    <div class="credentials">MAC, L.AC</div>
    <ul class="contact-list">
      <li>
        <svg viewBox="0 0 16 16" aria-hidden="true"><path fill="#158a84" d="M3.5 1.5l2.5 0 1 3.5-1.8 1.2a9 9 0 0 0 4.6 4.6L11 9l3.5 1v2.5c0 1-1 2-2 2C6.5 14.5 1.5 9.5 1.5 3.5c0-1 1-2 2-2z"/></svg>
        612-555-0193
      </li>
      <li>
        <svg viewBox="0 0 16 16" aria-hidden="true"><rect x="1" y="3" width="14" height="10" rx="1" fill="#158a84"/><path d="M1.5 4l6.5 5 6.5-5" fill="none" stroke="#fff" stroke-width="1.3"/></svg>
        info@needlenook-example.com
      </li>
      <li>
        <svg viewBox="0 0 16 16" aria-hidden="true"><circle cx="8" cy="8" r="7" fill="#158a84"/><path d="M1 8h14M8 1c-3 3.5-3 10.5 0 14M8 1c3 3.5 3 10.5 0 14" fill="none" stroke="#fff" stroke-width="1"/></svg>
        www.needlenook-example.com
      </li>
    </ul>
  </section>

  <section class="card card-back">
    <div class="brand"><span class="brand-dot"></span>NeedleNook</div>
    <div class="promo">FIRST SESSION FREE</div>
  </section>
</body>
</html>
```